Brell Harbor Company Business Cards

Front and Back Business Card - logo and text setup - cool design. I need workable photoshop or illustrator files so I can setup each employee card with design that is created
Updates

Hi everyone, thank you for the great entries. Please no more white and blue cards - there are so many already - black and silver only now please. thanks!

Target Market(s)

Construction Industry - Facility Managers

Industry/Entity Type

Construction

Contact Information for Business Card

I really like contemporary simplistic looks - clean neat....not opposed to seeing some black backrounds

Requirements
Must have
• Logo/website address with design on front only - www.brellharbor-example.com (logo attached)
• Back:
• Name/Title/Company Address/Phone/email address
Nice to have
• Cool design
Should not have
• Nothing gimmicky like Fire or Water - since we are a Fire Protection company - it has all been done

```html
<!DOCTYPE html>
<html lang="en">
<head>
<meta charset="utf-8">
<title>Brell Harbor Company Business Cards</title>
<link href="https://fonts.googleapis.com/css2?family=Open+Sans:wght@400;600;700;800&display=swap" rel="stylesheet">
<style>
  :root {
    --stage: #1c1c1e;
    --card: #050505;
    --brand-blue: #10239e;
    --brand-red: #ff2a26;
    --text-light: #f2f2f2;
    --text-muted: #d9d9d9;
    --divider: #8a8a8a;
  }
  * { box-sizing: border-box; margin: 0; padding: 0; }
  html, body {
    width: 1200px; height: 960px; overflow: hidden;
    background: var(--stage);
    font-family: "Open Sans", Arial, sans-serif;
  }
  .canvas { position: relative; width: 1200px; height: 960px; }
  .card {
    position: absolute; left: 320px; width: 560px; height: 320px;
    background: var(--card); overflow: hidden;
    box-shadow: 0 18px 40px rgba(0,0,0,.55);
  }
  .card--front { top: 70px; }
  .card--back { top: 500px; }

  .brand { display: flex; align-items: center; gap: 12px; }
  .brand__mark { width: 16px; height: 16px; background: var(--brand-blue); }
  .brand__name {
    font-weight: 800; color: var(--brand-red);
    letter-spacing: -0.5px; line-height: 1;
  }

  .card--front .brand { position: absolute; left: 0; right: 0; top: 112px; justify-content: center; }
  .card--front .brand__name { font-size: 48px; }
  .card--front .brand__mark { width: 22px; height: 22px; }
  .front__website {
    position: absolute; left: 0; right: 0; top: 206px; text-align: center;
    color: var(--text-light); font-size: 15px; letter-spacing: 3px;
  }

  .card--back .brand { position: absolute; left: 34px; top: 118px; }
  .card--back .brand__name { font-size: 32px; }
  .back__divider {
    position: absolute; left: 300px; top: 70px; width: 1px; height: 170px;
    background: var(--divider);
  }
  .contact { position: absolute; left: 318px; top: 72px; color: var(--text-light); }
  .contact__name { font-weight: 700; font-size: 17px; line-height: 1.15; }
  .contact__title { font-size: 15px; color: var(--text-muted); margin-bottom: 14px; }
  .contact__line { display: flex; align-items: center; gap: 8px; font-size: 13.5px; line-height: 22px; }
  .contact__icon { width: 12px; height: 12px; flex: none; }
  .contact__address { margin-top: 6px; font-size: 14.5px; line-height: 20px; }
  .back__stripe { position: absolute; left: 0; bottom: 0; width: 560px; height: 12px; }
</style>
</head>
<body>
<main class="canvas">
  <section class="card card--front" aria-label="Business card front">
    <div class="brand">
      <span class="brand__mark"></span>
      <span class="brand__name">Brell Harbor</span>
    </div>
    <p class="front__website">www.brellharbor-example.com</p>
  </section>

  <section class="card card--back" aria-label="Business card back">
    <div class="brand">
      <span class="brand__mark"></span>
      <span class="brand__name">Brell Harbor</span>
    </div>
    <div class="back__divider"></div>
    <div class="contact">
      <p class="contact__name">Dana Whitlow</p>
      <p class="contact__title">President</p>
      <p class="contact__line">
        <svg class="contact__icon" viewBox="0 0 12 12"><path d="M2.5 1 L4.5 1 L5.3 3.4 L4 4.3 Q5 6.8 7.7 8 L8.6 6.7 L11 7.5 L11 9.5 Q10.5 11 9 11 Q1 10 1 2.8 Q1 1.2 2.5 1 Z" fill="var(--brand-red)"/></svg>
        (555) 014-2290
      </p>
      <p class="contact__line">
        <svg class="contact__icon" viewBox="0 0 12 12"><rect x="0.5" y="2" width="11" height="8" fill="var(--brand-red)"/><path d="M0.8 2.3 L6 6.5 L11.2 2.3" fill="none" stroke="var(--card)" stroke-width="1.1"/></svg>
        info@brellharbor-example.com
      </p>
      <p class="contact__line">
        <svg class="contact__icon" viewBox="0 0 12 12"><g fill="none" stroke="var(--brand-red)" stroke-width="1.2"><circle cx="6" cy="6" r="5"/><ellipse cx="6" cy="6" rx="2.2" ry="5"/><path d="M1 6 H11"/></g></svg>
        www.brellharbor-example.com
      </p>
      <p class="contact__address">48 Keel Row Lane<br>Port Alder, NY 10990</p>
    </div>
    <svg class="back__stripe" viewBox="0 0 560 12" preserveAspectRatio="none" aria-hidden="true">
      <polygon points="0,0 268,0 280,12 0,12" fill="var(--brand-blue)"/>
      <polygon points="274,0 560,0 560,12 286,12" fill="var(--brand-red)"/>
    </svg>
  </section>
</main>
</body>
</html>
```